Maple Hollow Elementary School Letterhead

We would like a letterhead that includes our school mascot (Breezy the Falcon), school address, and phone number. We want something with personality and a little fun. Our school colors are navy blue, green (like the flag in our graphic), and gray. We included an example of a letterhead we like the feel of (on the fun side). The example is the image titled "sample." We are the Maple Hollow Falcons.
Maple Hollow Elementary
Address: 418 Fern Thistle, Brookvale, CA 95871
Phone: (949) 555-0173
maplehollow.tgsd-example.org

```html
<!DOCTYPE html>
<html lang="en">
<head>
<meta charset="utf-8">
<title>Maple Hollow Elementary — Letterhead</title>
<link rel="stylesheet" href="https://fonts.googleapis.com/css2?family=Montserrat:wght@400;500;700&display=swap">
<style>
  :root {
    --backdrop: #a3a3a3;
    --paper-light: #ffffff;
    --paper-shade: #ebebed;
    --ink: #3d3d3d;
    --ink-soft: #4a4a4a;
    --navy: #2c3e7a;
    --green: #3aaa48;
    --periwinkle: #8497c7;
    --rule-blue: #3b5bb5;
    --signature-tone: #d9d9dc;
  }
  html, body {
    margin: 0;
    padding: 0;
    width: 1200px;
    height: 1141px;
    overflow: hidden;
    background: var(--backdrop);
  }
  .letterhead {
    position: absolute;
    left: 209px;
    top: 20px;
    width: 782px;
    height: 1100px;
    background: linear-gradient(160deg, var(--paper-light) 35%, var(--paper-shade) 100%);
    box-shadow: 0 4px 14px rgba(0,0,0,0.25);
    font-family: "Montserrat", Arial, sans-serif;
    color: var(--ink);
    overflow: hidden;
  }
  .brand {
    position: absolute;
    left: 56px;
    top: 100px;
    height: 46px;
    display: flex;
    align-items: center;
    gap: 9px;
  }
  .brand-dot {
    width: 22px;
    height: 22px;
    border-radius: 50%;
    background: var(--navy);
  }
  .brand-name {
    font-weight: 700;
    font-size: 22px;
    color: var(--navy);
    letter-spacing: 0.3px;
    white-space: nowrap;
  }
  .header-rule {
    position: absolute;
    top: 113px;
    width: 1px;
    height: 33px;
    background: var(--rule-blue);
  }
  .header-rule.first { left: 336px; }
  .header-rule.second { left: 552px; }
  .contact {
    position: absolute;
    top: 117px;
    font-size: 10px;
    line-height: 13px;
    color: var(--ink);
    white-space: nowrap;
  }
  .contact p { margin: 0; }
  .contact.address { left: 366px; }
  .contact.reach { left: 579px; }
  .salutation {
    position: absolute;
    left: 58px;
    top: 274px;
    margin: 0;
    font-size: 19px;
    font-weight: 400;
    color: var(--ink-soft);
  }
  .letter-body {
    position: absolute;
    left: 58px;
    top: 331px;
    width: 667px;
    font-size: 11.7px;
    line-height: 16.6px;
    letter-spacing: 0.1px;
    color: var(--ink-soft);
    text-align: justify;
    hyphens: auto;
  }
  .letter-body p { margin: 0 0 17px; }
  .closing {
    position: absolute;
    left: 57px;
    top: 752px;
    margin: 0;
    font-size: 11.7px;
    color: var(--ink-soft);
  }
  .signature {
    position: absolute;
    left: 53px;
    top: 784px;
    width: 226px;
    height: 64px;
    background: var(--signature-tone);
    border-radius: 4px;
  }
  .color-bands {
    position: absolute;
    left: 0;
    bottom: 0;
    width: 100%;
    height: 19px;
    display: flex;
    gap: 3px;
  }
  .color-bands span { flex: 1; }
  .band-navy { background: var(--navy); }
  .band-green { background: var(--green); }
  .band-periwinkle { background: var(--periwinkle); }
</style>
</head>
<body>
  <main class="letterhead">
    <header>
      <div class="brand">
        <span class="brand-dot"></span>
        <span class="brand-name">Maple Hollow</span>
      </div>
      <span class="header-rule first"></span>
      <div class="contact address">
        <p>Maple Hollow Elementary</p>
        <p>418 Fern Thistle, Brookvale, CA 95871</p>
      </div>
      <span class="header-rule second"></span>
      <div class="contact reach">
        <p>(707) 555-0173</p>
        <p>www.maplehollow.tgsd-example.org</p>
      </div>
    </header>

    <h1 class="salutation">Dear Mr. Hadley,</h1>

    <section class="letter-body">
      <p>Lorem ipsum dolor sit amet, consectetur adipiscing elit. Donec orci purus, luctus vitae dignissim eu, iaculis sed purus. Vivamus faucibus, ipsum nec aliquet viverra, leo mauris condimentum ligula, sit amet sagittis enim ligula quis arcu. Nam egestas tortor id nisi porttitor mattis. In tortor ante, ultricies in suscipit a, tempus non massa. Vivamus et auctor mi. Fusce vel massa nulla. Phasellus nec eros mauris, et scelerisque orci.</p>
      <p>Donec malesuada orci vitae nulla accumsan porta a id massa. Quisque accumsan iaculis magna sit amet fringilla. Maecenas consequat, magna eget tincidunt semper, odio nibh rutrum mi, id feugiat ante nisi eu risus. Vestibulum nunc orci, rhoncus a placerat in, ultricies in mi. Cras mattis varius eros, vel fringilla nisi suscipit eget. Quisque scelerisque sagittis nulla at porttitor.</p>
      <p>Sed id augue vitae urna euismod commodo aliquet a quam. Pellentesque arcu velit, cursus et malesuada ut, consequat et diam. Nullam erat sem, rhoncus id ullamcorper vitae, rhoncus et arcu. In ultricies ultricies nulla, ut rutrum nisi iaculis at. Donec eu magna a metus ornare faucibus. Fusce aliquet faucibus ultricies. Morbi semper, est id tincidunt gravida, sem arcu adipiscing lacus, ac bibendum nulla leo eu purus. Quisque nec diam sed risus consectetur a ccumsan quis quis nibh. Vestibulum id purus lorem.</p>
      <p>It is a long established fact that a reader will be distracted by the readable content of a page when looking at its layout. The point of using Lorem Ipsum is that it has a more-or-less normal distribution of letters, as opposed to using 'Content here, content here', making it look like readable English. Many desktop publishing packages</p>
      <p>ada ut, consequat et diam. Nullam erat sem, rhoncus id ullamcorper vitae, rhoncus et arcu. In ultricies ultricies nulla, ut rutrum nisi iaculis at. Donec eu magna a metus ornare faucibus. Fusce aliquet faucibus ultricies. Morbi semper,</p>
    </section>

    <p class="closing">Sincerely,</p>
    <div class="signature" role="img" aria-label="Handwritten signature of the principal"></div>

    <footer class="color-bands">
      <span class="band-navy"></span>
      <span class="band-green"></span>
      <span class="band-periwinkle"></span>
    </footer>
  </main>
</body>
</html>
```